Software Company Business Card

We are looking for a new design of our business card. The design will also be used in the rest of our branding and marketing materials as we want to keep it all uniform. We sell POS software to fine/luxury jewelers and also offer other business services as well to help the jeweler manage their business and need something more updated, technical and fresh, preferably more on the masculine side. We do not want any designs with gems in them but if possible would like to incorporate the circle and arrow in the logo into the design, but not a requirement if you can't make it work. I would like to see a variety of the mix. The colors need to remain our blue and orange and the logo can not change. The squiggly lines have been used as our corporate identity for over 20 years and its time to update. Our company name is PELK (Bright Ledger Counter Solutions).

Target Market(s)

High End Jewelers

Industry/Entity Type

Software

Contact Information for Business Card

Requirements
Must have
• Our logo and the colors must remain the same. Blue is #d95d39 and Orange is #0f5682.
Nice to have
• The circle and arrow incorporated but not a requirement.
Should not have
• Anything jewelry or gem related.

```html
<!DOCTYPE html>
<html lang="en">
<head>
<meta charset="utf-8">
<title>PELK Business Card</title>
<link rel="stylesheet" href="https://fonts.googleapis.com/css2?family=Open+Sans:wght@400&family=Source+Sans+3:wght@400;600;700&display=swap">
<style>
  :root {
    --brand-blue: #135785;
    --brand-orange: #dd603d;
    --soft-grey: #f2f2f4;
    --text-grey: #6b6b6b;
    --card-white: #ffffff;
    --stage: #2b2b2b;
  }
  * { margin: 0; padding: 0; box-sizing: border-box; }
  html, body {
    width: 1200px; height: 582px; overflow: hidden;
    background: var(--stage);
  }
  .card {
    position: absolute;
    width: 465px; height: 279px;
    background: var(--card-white);
    overflow: hidden;
    box-shadow: 0 4px 10px rgba(0,0,0,.45);
  }
  .card--front { left: 104px; top: 153px; }
  .card--back  { left: 631px; top: 150px; }

  .accent-circle {
    position: absolute; border-radius: 50%;
  }
  .card--front .accent-circle {
    width: 276px; height: 276px; left: 246px; top: 97px;
    background: var(--soft-grey);
  }
  .card--back .accent-circle {
    width: 282px; height: 282px; left: 243px; top: 96px;
    background: var(--brand-blue);
  }

  .wordmark {
    position: absolute; left: 43px; top: 90px;
    display: flex; align-items: center; gap: 12px;
  }
  .wordmark__name {
    font-family: "Source Sans 3", sans-serif;
    font-weight: 700; font-size: 42px; line-height: 1;
    color: var(--brand-blue); letter-spacing: 1px;
  }
  .wordmark__dot {
    width: 41px; height: 41px; border-radius: 50%;
    background: var(--brand-orange);
  }

  .address {
    position: absolute; left: 39px; top: 145px;
    font-family: "Open Sans", sans-serif;
    font-size: 12.5px; line-height: 17px;
    letter-spacing: 0.9px; color: var(--text-grey);
  }

  .person { position: absolute; left: 39px; top: 64px; font-family: "Source Sans 3", sans-serif; }
  .person__name {
    font-weight: 600; font-size: 24px; line-height: 1.05;
    color: var(--brand-blue);
  }
  .person__title {
    font-size: 12.5px; color: var(--text-grey); margin-top: 1px;
  }

  .contact-list {
    position: absolute; left: 39px; top: 117px; list-style: none;
    font-family: "Source Sans 3", sans-serif;
  }
  .contact-list__item {
    display: flex; align-items: center; gap: 7px;
    height: 26px; font-size: 17px; color: var(--text-grey);
  }
  .contact-list__icon { width: 13px; height: 13px; flex: none; }
</style>
</head>
<body>
  <section class="card card--front">
    <div class="accent-circle"></div>
    <div class="wordmark">
      <span class="wordmark__name">PELK</span>
      <span class="wordmark__dot"></span>
    </div>
    <p class="address">1480 Meridian Parkway Suite 210<br>Henderson, NV 89052 USA</p>
  </section>

  <section class="card card--back">
    <div class="accent-circle"></div>
    <div class="person">
      <h1 class="person__name">Dorian Whitfield</h1>
      <p class="person__title">Director of Global Operations</p>
    </div>
    <ul class="contact-list">
      <li class="contact-list__item">
        <svg class="contact-list__icon" viewBox="0 0 14 14"><circle cx="7" cy="7" r="7" fill="#dd603d"/><path d="M4.3 3.6c.4-.4.9-.3 1.1.1l.6 1.2c.2.4 0 .7-.3.9-.2.2-.2.4 0 .8.4.7.9 1.2 1.6 1.6.4.2.6.2.8 0 .2-.3.5-.5.9-.3l1.2.6c.4.2.5.7.1 1.1-.7.8-1.8.9-3 .2C5.8 9 5 8.2 4.3 6.7c-.6-1.2-.6-2.3 0-3.1z" fill="#fff"/></svg>
        +1 800 555-0142
      </li>
      <li class="contact-list__item">
        <svg class="contact-list__icon" viewBox="0 0 14 14"><circle cx="7" cy="7" r="7" fill="#dd603d"/><rect x="4.8" y="3.3" width="4.4" height="2.2" fill="none" stroke="#fff" stroke-width=".9"/><rect x="3.5" y="5.5" width="7" height="3.4" rx=".6" fill="none" stroke="#fff" stroke-width=".9"/><rect x="4.8" y="7.6" width="4.4" height="2.8" fill="#fff"/></svg>
        +1 702 555-0187
      </li>
      <li class="contact-list__item">
        <svg class="contact-list__icon" viewBox="0 0 14 14"><circle cx="7" cy="7" r="7" fill="#dd603d"/><rect x="3.5" y="4.5" width="7" height="5" fill="#fff"/><path d="M3.5 4.7 7 7.4l3.5-2.7" fill="none" stroke="#dd603d" stroke-width=".8"/></svg>
        dorian@pelkusa.com
      </li>
      <li class="contact-list__item">
        <svg class="contact-list__icon" viewBox="0 0 14 14"><circle cx="7" cy="7" r="7" fill="#dd603d"/><g fill="none" stroke="#fff" stroke-width=".7"><circle cx="7" cy="7" r="3.8"/><ellipse cx="7" cy="7" rx="1.6" ry="3.8"/><path d="M3.2 7h7.6M3.7 5.2h6.6M3.7 8.8h6.6"/></g></svg>
        www.pelkusa.com
      </li>
    </ul>
  </section>
</body>
</html>
```